Ironvale Holdings Business card

We need a an amazing matte black and gold card! W are a finance investing company so we want something that's eye catching and sleek. We want it to be attractive and sleek and represent money. Heck with would like the letters and lgo to be printed as 24k gold one day. We have the logo added so please use the color scheme with the logo and have that beautifully placed on one side.

Target Market(s)

Investors of all ages

Industry/Entity Type

Financial

Contact Information for Business Card

Black and matte with gold lettering follow logo colrs please.

Font styles to use
Other font styles liked:
• you decide

Colors

Designer to choose colors to be used in the design.

Requirements
Must have
• Matte Black and Gold, logo on one side. job title and name , website, phone number and email address on the other side
Nice to have
• Matte black and crisp finish to attract investors
Should not have
• playful, very professional!

```html
<!DOCTYPE html>
<html lang="en">
<head>
<meta charset="utf-8">
<title>Ironvale Holdings Business Card</title>
<link rel="stylesheet" href="https://fonts.googleapis.com/css2?family=Open+Sans:wght@400;700&display=swap">
<style>
  :root {
    --backdrop: #2e2724;
    --card-black: #262626;
    --card-edge: #1b1b1b;
    --gold: #d4a81c;
    --gold-line: #b8950f;
    --text-light: #f2f2f2;
  }
  * { margin: 0; padding: 0; box-sizing: border-box; }
  html, body {
    width: 1200px; height: 847px; overflow: hidden;
    background: var(--backdrop);
    font-family: "Open Sans", Arial, sans-serif;
  }
  .canvas { position: relative; width: 1200px; height: 847px; }
  .card {
    position: absolute; width: 525px; height: 300px;
    background: var(--card-black);
    border: 1px solid var(--card-edge);
    box-shadow: 0 10px 24px rgba(0,0,0,0.45);
  }
  .card-front { left: 60px; top: 110px; }
  .card-back { left: 615px; top: 430px; }

  .wordmark {
    color: var(--gold); font-weight: 400;
    text-transform: uppercase; text-align: center; line-height: 1.15;
  }
  .card-front .wordmark {
    position: absolute; left: 0; right: 0; top: 108px;
    font-size: 34px; letter-spacing: 3px;
  }
  .wordmark .sub { display: block; font-size: 0.5em; letter-spacing: 0.55em; margin-top: 4px; }
  .card-back .wordmark {
    position: absolute; right: 34px; top: 38px;
    font-size: 25px; letter-spacing: 2px; text-align: center;
  }

  .holder { position: absolute; left: 30px; top: 40px; }
  .holder-name { color: var(--gold); font-weight: 700; font-size: 19px; letter-spacing: 0.5px; text-transform: uppercase; }
  .holder-role { color: var(--text-light); font-size: 14px; margin-top: -2px; }

  .divider {
    position: absolute; left: 24px; right: 52px; top: 120px;
    height: 1px; background: var(--gold-line);
  }

  .contact-list { position: absolute; left: 26px; top: 140px; list-style: none; }
  .contact-list li {
    display: flex; align-items: center; gap: 6px;
    color: var(--text-light); font-size: 14px; line-height: 21px;
  }
  .contact-list svg { width: 11px; height: 11px; fill: var(--gold); flex: none; }

  .address {
    position: absolute; right: 34px; bottom: 30px;
    color: var(--text-light); font-size: 15px; text-align: right; line-height: 21px;
  }
</style>
</head>
<body>
<main class="canvas">
  <section class="card card-front" aria-label="Card front">
    <p class="wordmark">Ironvale<span class="sub">Holdings</span></p>
  </section>

  <section class="card card-back" aria-label="Card back">
    <div class="holder">
      <p class="holder-name">Daniel Harlow</p>
      <p class="holder-role">Director</p>
    </div>
    <p class="wordmark">Ironvale<span class="sub">Holdings</span></p>
    <div class="divider"></div>
    <ul class="contact-list">
      <li>
        <svg viewBox="0 0 24 24" aria-hidden="true"><path d="M6.6 10.8a15.1 15.1 0 0 0 6.6 6.6l2.2-2.2c.3-.3.7-.4 1-.2 1.1.4 2.3.6 3.6.6.6 0 1 .4 1 1V20c0 .6-.4 1-1 1A17 17 0 0 1 3 4c0-.6.4-1 1-1h3.5c.6 0 1 .4 1 1 0 1.3.2 2.5.6 3.6.1.3 0 .7-.2 1z"/></svg>
        123 555 0148
      </li>
      <li>
        <svg viewBox="0 0 24 24" aria-hidden="true"><path d="M2 5h20v14H2z M2 5l10 8 10-8" /></svg>
        info@ironvaleholdings.com
      </li>
      <li>
        <svg viewBox="0 0 24 24" aria-hidden="true"><circle cx="12" cy="12" r="10"/></svg>
        www.ironvaleholdings.com
      </li>
    </ul>
    <p class="address">Rue des Tilleuls 14<br>Lausanne, Vaud 1004, CH</p>
  </section>
</main>
</body>
</html>
```